Yoga Training Cerificate

Design a certificate of graduation from a Vinyasa Yoga Teacher Training Program.

The attached document is an example of the certificate I received as a graduate from a teacher training program. You can use it as a template.

Stylistically, what you design can be: visually enticing, professional, clean, and modern.

Please develop the "Tidal Lotus" logo and embed it within the certificate.

Please add a circular watermark behind the body of the certificate similar to the one found in the attachment; leave out the words Asana Guild because I am not associated with that organization.

The name of my school is "Tidal Lotus." And it was established in 2017, which you can include.

The certificate affirms that "' 'such-and-such' has successfully completed the Tidal Lotus modern vinyasa yoga training, completing two hundred hours of instruction in practice and theory. Within the power of our institution as a certifying agent we declare Such-and-such, now, a teacher competent to share the gift of yoga with the masses in a safe and effective."

My name -Dennis Halvorsen- should be at bottom with a faux-signature; position title: Tidal Lotus founder.

If you decide to include text on the fringe, like the example, it might include bars of text describing the maxims of the Tidal Lotus school reading:

This is Tidal Lotus
Breath is primary
Evolve the physical culture
Bring your unique expression to the practice
Take Breaks
Freestyle
Close your eyes
Feel deeper into your body
This is active meditation
This is moving meditation
This is modern meditation

And find a way to integrate Emojis like: Fire, Water, Prayer Hands, etc. as you see fit.

Generally, make the certificate look: official, clear and clean. You can base it from the example given. And try and create a graphic design that is more visually capturing then the example.

```html
<!DOCTYPE html>
<html lang="en">
<head>
<meta charset="utf-8">
<title>Tidal Lotus — Certificate of Completion</title>
<link rel="stylesheet" href="https://fonts.googleapis.com/css2?family=Cinzel:wght@400&family=Open+Sans:wght@300;400&family=Tinos:ital@1&display=swap">
<style>
  :root {
    --page: #ffffff;
    --paper: #fcf9f3;
    --paper-line: rgba(200, 190, 170, 0.10);
    --teal: #24626a;
    --slate: #565656;
    --ink: #4a4a4a;
    --rule: #cfe0dc;
    --wash-top: #cfe6f0;
    --wash-soft: rgba(207, 230, 240, 0);
    --mandala: #b9d2d8;
    --seal: rgba(205, 225, 232, 0.35);
  }
  * { margin: 0; padding: 0; box-sizing: border-box; }
  html, body { width: 1200px; height: 1200px; overflow: hidden; background: var(--page); }
  .canvas { position: relative; width: 1200px; height: 1200px; }

  .certificate {
    position: absolute; left: 30px; top: 146px; width: 1114px; height: 824px;
    background-color: var(--paper);
    background-image: repeating-linear-gradient(-30deg, var(--paper-line) 0 1px, transparent 1px 7px);
    overflow: hidden;
  }
  .watercolor-wash {
    position: absolute; left: 0; top: 0; width: 1114px; height: 330px;
    background:
      radial-gradient(ellipse 360px 240px at 1000px 120px, var(--wash-top), var(--wash-soft)),
      radial-gradient(ellipse 300px 150px at 120px 120px, var(--wash-top), var(--wash-soft)),
      linear-gradient(180deg, rgba(207,230,240,0.65), rgba(207,230,240,0) 60%);
  }
  .mandala {
    position: absolute; border-radius: 50%;
    background: radial-gradient(circle, var(--mandala) 0 18%, rgba(185,210,216,0.55) 40%, rgba(185,210,216,0) 70%);
  }
  .mandala-top-left { left: -140px; top: -90px; width: 360px; height: 360px; }
  .mandala-bottom-right { left: 880px; top: 580px; width: 360px; height: 360px; }

  .seal { position: absolute; left: 0; top: 0; }

  .title {
    position: absolute; left: 0; width: 1114px; top: 72px; text-align: center;
    font-family: "Cinzel", serif; font-weight: 400; font-size: 76px;
    letter-spacing: 13px; color: var(--teal); line-height: 1;
  }
  .subtitle {
    position: absolute; left: 0; width: 1114px; top: 142px;
    display: flex; justify-content: center; align-items: center; gap: 18px;
  }
  .subtitle-text {
    font-family: "Open Sans", sans-serif; font-weight: 400; font-size: 48px;
    color: var(--slate); letter-spacing: 2px; line-height: 1;
  }
  .subtitle-rule { width: 124px; height: 8px; position: relative; }
  .subtitle-rule::before, .subtitle-rule::after {
    content: ""; position: absolute; height: 1px; background: var(--slate);
  }
  .subtitle-rule::before { left: 0; right: 0; top: 1px; }
  .subtitle-rule::after { left: 50px; right: 0; top: 6px; }
  .subtitle-rule.right::after { left: 0; right: 50px; }

  .school-name {
    position: absolute; left: 0; width: 1114px; top: 302px; text-align: center;
    font-family: "Open Sans", sans-serif; font-weight: 400; font-size: 52px;
    color: var(--teal); line-height: 1;
  }
  .school-name::before {
    content: ""; display: block; width: 46px; height: 46px; border-radius: 50%;
    background: var(--teal); margin: -80px auto 34px;
  }

  .date-line {
    position: absolute; left: 104px; top: 428px; width: 920px;
    font-family: "Tinos", serif; font-style: italic; font-size: 32px; line-height: 40px; color: var(--ink);
    display: flex; align-items: flex-end; white-space: nowrap;
  }
  .blank { display: inline-block; border-bottom: 1px solid var(--rule); height: 1px; margin-bottom: 8px; }
  .blank-day { width: 190px; margin-left: 24px; margin-right: 12px; }
  .blank-month { width: 300px; margin-left: 20px; }
  .blank-year { width: 146px; margin-left: 8px; }

  .name-line { position: absolute; left: 104px; top: 528px; width: 898px; height: 1px; background: var(--rule); }

  .statement {
    position: absolute; left: 104px; top: 558px; width: 904px;
    font-family: "Tinos", serif; font-style: italic; font-size: 31px; line-height: 52px; color: var(--ink);
  }
  .statement .line { display: block; white-space: nowrap; }
  .statement .full { text-align: justify; text-align-last: justify; }
  .statement .tight { letter-spacing: -0.3px; }

  .signature-rule { position: absolute; left: 301px; top: 748px; width: 469px; height: 1px; background: var(--rule); }
  .signatory {
    position: absolute; left: 301px; width: 469px; top: 754px; text-align: center;
    font-family: "Open Sans", sans-serif; font-weight: 300; font-size: 28px; line-height: 36px; color: var(--ink);
  }
</style>
</head>
<body>
<div class="canvas">
  <section class="certificate">
    <div class="watercolor-wash" role="img" aria-label="Soft blue watercolour wash across the top"></div>
    <div class="mandala mandala-top-left" role="img" aria-label="Pale blue mandala ornament"></div>
    <div class="mandala mandala-bottom-right" role="img" aria-label="Pale blue-grey mandala ornament"></div>

    <svg class="seal" width="1114" height="824" viewBox="0 0 1114 824" aria-hidden="true">
      <circle cx="558" cy="486" r="224" fill="none" stroke="var(--seal)" stroke-width="16"/>
    </svg>

    <h1 class="title">CERTIFICATE</h1>
    <div class="subtitle">
      <span class="subtitle-rule left"></span>
      <span class="subtitle-text">OF COMPLETION</span>
      <span class="subtitle-rule right"></span>
    </div>

    <div class="school-name">TIDAL LOTUS</div>

    <p class="date-line">
      <span>On this</span><span class="blank blank-day"></span>
      <span>day of</span><span class="blank blank-month"></span><span>,</span>
      <span class="blank blank-year"></span><span>.</span>
    </p>

    <div class="name-line"></div>

    <p class="statement">
      <span class="line full">has successfully completed the Tidal Lotus modern vinyasa yoga</span>
      <span class="line full tight">training, completing two hundred hours of instruction in practice and</span>
      <span class="line">theory.</span>
    </p>

    <div class="signature-rule"></div>
    <p class="signatory">Tidal Lotus founder</p>
  </section>
</div>
</body>
</html>
```